Bold Cover needed for a book on Workplace Bullying

I need a book cover design for a book titled, “Iron Silence?” The book recounts my story of bullying in the workplace. It also includes chapters on how readers can minimize/stop workplace bullying, write an effective complaint, and ensure their own mental wellbeing.
I am looking for a bold design using red and black, and possibly distressed lettering. The covers of other books dealing with this subject do not reflect my vision. They are often too childish or look too academic. This book needs to stress the serious nature of a toxic workplace, while appealing to readers experiencing a similar situation. I’d like the cover to reflect the mental anguish associated with workplace bullying (hence the distressed lettering).
I have included a cover that appeals to me (although the coloring is wrong). That said, I am also very happy (and excited) to see your creative input!
On the cover, it should have the following:
Title: Iron Silence?
Subtitle: How the Harbour Works Department Condones Bullying & Ruins Lives
Author: Owen Frick
Other relevant details:
Book size: 5.5” x 8.5”
Back cover will have a blurb, author picture/short bio, and barcode
The blurb on the back cover reads:
Undermining, intimidation and threats
Despite the Department of Harbour Works allegedly holding a zero tolerance for bullying, these behaviours were an everyday occurrence in at least one workplace. Even after a decade of complaints, numerous witnesses and physical proof, the department failed to act. Instead, they looked the other way, allowing one powerful and well-connected individual to end careers and ruin lives.
After being targeted, one teacher resolved to put an end to the abuse experienced by more than fifty employees. His startling story reveals the relentless bullying, mental health ramifications, and insidious tactics used to cover up the corrosive behaviour.
Those who have experienced a toxic workplace will also find much needed support and guidance, intended to minimise suffering and detail a clear way forward. Chapters include dealing with bullying in the workplace, how to lodge a successful complaint, and how to stay sane during any potential legal action.

```html
<!DOCTYPE html>
<html lang="en">
<head>
<meta charset="utf-8">
<title>Iron Silence? — Owen Frick</title>
<link rel="stylesheet" href="https://fonts.googleapis.com/css2?family=Barlow+Condensed:wght@600;700&family=Rubik+Dirt&display=swap">
<style>
  :root {
    --stage: #000000;
    --paper: #ffffff;
    --ink: #222222;
    --title-ink: #2a2a2a;
    --hand-red: #f20d0d;
  }
  * { margin: 0; padding: 0; box-sizing: border-box; }
  html, body {
    width: 1200px;
    height: 1200px;
    overflow: hidden;
    background: var(--stage);
  }
  .cover {
    position: absolute;
    left: 212px;
    top: 0;
    width: 776px;
    height: 1200px;
    background: var(--paper);
    overflow: hidden;
  }
  .subtitle {
    position: absolute;
    top: 55px;
    left: 0;
    width: 100%;
    text-align: center;
    font-family: "Barlow Condensed", sans-serif;
    font-weight: 700;
    font-size: 37px;
    line-height: 46px;
    letter-spacing: 2.4px;
    color: var(--ink);
    text-transform: uppercase;
  }
  .handprint-area {
    position: absolute;
    left: 0;
    top: 0;
    width: 776px;
    height: 1200px;
  }
  .title-art {
    position: absolute;
    left: 0;
    top: 0;
    width: 776px;
    height: 1200px;
  }
  .title-line {
    font-family: "Rubik Dirt", sans-serif;
    fill: var(--title-ink);
    stroke: var(--paper);
    stroke-width: 3px;
    paint-order: stroke;
  }
  .author {
    position: absolute;
    top: 1063px;
    left: 0;
    width: 100%;
    text-align: center;
    font-family: "Barlow Condensed", sans-serif;
    font-weight: 700;
    font-size: 86px;
    line-height: 86px;
    letter-spacing: 9px;
    color: var(--ink);
    text-transform: uppercase;
  }
</style>
</head>
<body>
  <main class="cover">
    <p class="subtitle">How the Harbour Works Department<br>Condones Bullying &amp; Ruins Lives</p>

    <svg class="handprint-area" viewBox="0 0 776 1200" role="img" aria-label="Large red painted handprint with fingers spread, raised as a stop gesture">
      <defs>
        <radialGradient id="handGlow" cx="390" cy="610" r="400" gradientUnits="userSpaceOnUse" gradientTransform="translate(390 610) scale(0.88 1.05) translate(-390 -610)">
          <stop offset="0" stop-color="var(--hand-red)"/>
          <stop offset="0.62" stop-color="var(--hand-red)"/>
          <stop offset="1" stop-color="var(--hand-red)" stop-opacity="0"/>
        </radialGradient>
      </defs>
      <rect x="0" y="180" width="776" height="860" fill="url(#handGlow)"/>
    </svg>

    <svg class="title-art" viewBox="0 0 776 1200" aria-label="Iron Silence?">
      <text class="title-line" x="143" y="700" font-size="290" textLength="525" lengthAdjust="spacingAndGlyphs">IRON</text>
      <text class="title-line" x="50" y="845" font-size="165" textLength="678" lengthAdjust="spacingAndGlyphs">SILENCE?</text>
    </svg>

    <p class="author">Owen Frick</p>
  </main>
</body>
</html>
```